Business Card Design for Orthopaedic Surgeon

This is a double-sided glossy business card. I prefer baby blue, teal, and green as color schemes. I have my logo already (many colors that you can choose from). I have photos and examples of my old card (very bland but has the information in it). I also have one that my assistant tried to design, but the writing is too small and I don't love the formatting. But it is close!
I would like my logo to be on the business card but I'm uploading my logo in many different colors so you can choose which one looks best based on the color scheme. I also uploaded many sized headshots so you can choose the best resolution one.

Additional information:
Correct business address:
4382 SE 58th Lane, Suite 305
Tamarac, FL 33347

Everything else on both business cards are accurate.

I actually need 2 different business cards generated. One that includes my cell phone number-- Personal cell: 585-614-3908 in addition to Office phone: (954) 362-5804 and Office Fax: 954-362-5819. Again, one card would have my personal cell and one wouldn't

Overall I just think the baby blue card (uploaded) is missing something on the front--of course it is also missing my office phone/fax/personal cell. I do want my website on the front too. Email: info@rkellowsurg.com

You can use your discretion about what goes on the front vs. what goes on the back to eliminated clutter.

Oh and on the back, I would like to list "Conditions Treated" (not specialties include). The list is:
Carpal Tunnel
Trigger Finger
Ganglion Cysts
Hand Tumors
Han & Wrist Arthritis
Hand, Wrist & Elbow Tendonitis
Fractures of the Hand, Wrist, Elbow and Humerus
Nerve Injuries of the Hand, Wrist & Elbow
Microsurgery
Wrist Arthroscopy
Endoscopic Surgery

Target Market(s)

Primary care doctors, Lawyers, patients

Industry/Entity Type

Medical

Contact Information for Business Card

Please see above in project description

Colors

Requirements
Must have
• -Correct office info, Board Certified Orthopaedic Hand & Upper Extremity Surgeon
Nice to have
• Something that is classy and wow!

```html
<!DOCTYPE html>
<html lang="en">
<head>
<meta charset="utf-8">
<title>Renata Kellow, M.D. — Business Card</title>
<link rel="stylesheet" href="https://fonts.googleapis.com/css2?family=Montserrat:wght@400;500;600;700&display=swap">
<style>
  :root {
    --teal: #00807e;
    --teal-dark: #006e6c;
    --sky: #2a8fd4;
    --ink: #111111;
    --white: #ffffff;
    --gold: #c9a66b;
    --page: #e9e6e1;
    --photo-top: #d9d4cf;
    --photo-bottom: #3a2c25;
  }
  * { box-sizing: border-box; margin: 0; padding: 0; }
  html, body { width: 900px; height: 1200px; overflow: hidden; }
  body {
    background: var(--page);
    font-family: "Montserrat", Arial, sans-serif;
    position: relative;
  }
  .card {
    position: absolute;
    left: 80px;
    width: 742px;
    height: 440px;
    border-radius: 28px;
    overflow: hidden;
    box-shadow: 0 6px 16px rgba(0,0,0,0.25);
  }
  .card--front { top: 132px; background: var(--white); }
  .card--back { top: 638px; background: var(--teal); }

  /* Front */
  .brand {
    position: absolute; left: 34px; top: 30px;
    width: 156px; height: 156px;
    display: flex; align-items: center; justify-content: center;
    border: 4px solid var(--ink); border-radius: 50%;
  }
  .brand__name {
    font-weight: 700; font-size: 26px; letter-spacing: 2px;
    color: var(--ink); text-align: center; line-height: 1.1;
  }
  .name-band {
    position: absolute; left: 28px; top: 204px;
    width: 462px; height: 63px;
    background: var(--teal); color: var(--white);
    padding: 4px 0 0 10px;
  }
  .name-band__name { font-weight: 600; font-size: 24px; line-height: 30px; }
  .name-band__title { font-weight: 400; font-size: 15.5px; line-height: 20px; }
  .contacts {
    position: absolute; left: 38px; top: 280px;
    list-style: none;
  }
  .contacts li {
    display: flex; align-items: center; gap: 11px;
    font-size: 16px; line-height: 24.5px; color: var(--ink);
  }
  .contacts svg { width: 16px; height: 16px; fill: var(--teal); flex: none; }
  .headshot {
    position: absolute; left: 435px; top: 18px;
    width: 307px; height: 360px;
    background: linear-gradient(180deg, var(--photo-top) 0%, #9a7c6a 45%, var(--photo-bottom) 100%);
  }
  .footer-shapes { position: absolute; left: 0; bottom: 0; width: 742px; height: 70px; }
  .address {
    position: absolute; right: 32px; bottom: 14px;
    text-align: right; color: var(--white);
    font-size: 16px; line-height: 20px;
  }

  /* Back */
  .conditions { position: absolute; left: 36px; top: 142px; color: var(--white); }
  .conditions__title { font-weight: 600; font-size: 25px; line-height: 32px; margin-bottom: 14px; }
  .conditions__list { list-style: none; }
  .conditions__list li {
    font-size: 16px; line-height: 19.6px; padding-left: 19px; position: relative;
  }
  .conditions__list li::before {
    content: ""; position: absolute; left: 2px; top: 8px;
    width: 5px; height: 5px; border-radius: 50%; background: var(--white);
  }
  .brand--gold {
    left: 452px; top: 48px; width: 214px; height: 214px;
    border: 4px solid var(--gold);
  }
  .brand--gold .brand__name { color: var(--gold); font-size: 34px; }
</style>
</head>
<body>

<section class="card card--front">
  <div class="brand"><span class="brand__name">RK<br>HAND</span></div>

  <div class="name-band">
    <h1 class="name-band__name">Renata Kellow, M.D.</h1>
    <p class="name-band__title">Hand and upper extremity specialist</p>
  </div>

  <ul class="contacts">
    <li><svg viewBox="0 0 16 16"><path d="M1 6c0-2 3-4 7-4s7 2 7 4v1h-4V5.5H5V7H1z"/><path d="M3 8h10l1 6H2z"/></svg>(954) 362-5804</li>
    <li><svg viewBox="0 0 16 16"><path d="M4 0h8a1 1 0 0 1 1 1v14a1 1 0 0 1-1 1H4a1 1 0 0 1-1-1V1a1 1 0 0 1 1-1zm1 2v10h6V2zm3 11a1 1 0 1 0 0 2 1 1 0 0 0 0-2z"/></svg>585-614-3908</li>
    <li><svg viewBox="0 0 16 16"><path d="M1 5h3v10H1zM5 1h7l2 2v3H5zM5 7h10v8H5zm2 2v1.5h2V9zm4 0v1.5h2V9zm-4 3v1.5h2V12zm4 0v1.5h2V12z"/></svg>954-362-5819</li>
    <li><svg viewBox="0 0 16 16"><path d="M1 3h14v1.5L8 9 1 4.5z"/><path d="M1 6.3 8 10.8l7-4.5V13H1z"/></svg>info@rkellowsurg.com</li>
  </ul>

  <div class="headshot" role="img" aria-label="Headshot portrait of Dr. Renata Kellow in a dark blazer"></div>

  <svg class="footer-shapes" viewBox="0 0 742 70" aria-hidden="true">
    <path d="M0 18 H368 L355 44 H0 Z" fill="var(--sky)"/>
    <path d="M0 44 H355 L350 52 H0 Z" fill="var(--white)"/>
    <path d="M400 6 H742 V70 H0 V56 H352 C362 56 366 50 372 34 C380 14 386 6 400 6 Z" fill="var(--teal)"/>
  </svg>

  <p class="address">4382 SE 58th Lane, Suite 305<br>Tamarac, FL 33347</p>
</section>

<section class="card card--back">
  <div class="conditions">
    <h2 class="conditions__title">Conditions Treated</h2>
    <ul class="conditions__list">
      <li>Carpal Tunnel</li>
      <li>Trigger Finger</li>
      <li>Ganglion Cysts</li>
      <li>Hand Tumors</li>
      <li>Han &amp; Wrist Arthritis</li>
      <li>Hand, Wrist &amp; Elbow Tendonitis</li>
      <li>Fractures of the Hand, Wrist, Elbow and Humerus</li>
      <li>Nerve Injuries of the Hand, Wrist &amp; Elbow</li>
      <li>Microsurgery</li>
      <li>Wrist Arthroscopy</li>
      <li>Endoscopic Surgery</li>
    </ul>
  </div>

  <div class="brand brand--gold"><span class="brand__name">RK<br>HAND</span></div>
</section>

</body>
</html>
```